Two-Sided Flyer - Architectural and Engineering Firm

Looking for a two-sided flyer that can be used at trade shows and initial meetings with new prospective clients that will highlight the services of our company as well as project photos of the type of work we do. You can find information and portfolio photos for your design ideas on our website at www.halvernquistodell.com

Target Market(s)

K-12 School Corporations

Industry/Entity Type

Architectural

Colors

Designer to choose colors to be used in the design.

Requirements
Must have
• Company logo, project photos that highlight the work we do, contact information, brief highlight of services we offer

```html
<!DOCTYPE html>
<html lang="en">
<head>
<meta charset="utf-8">
<title>Our Services – Halvernquist-Odell</title>
<link href="https://fonts.googleapis.com/css2?family=Oswald:wght@400;500&family=Open+Sans:ital,wght@0,400;0,600;1,400&display=swap" rel="stylesheet">
<style>
  :root{
    --green:#6f9a2c;
    --orange:#d9822b;
    --text:#3b3b3b;
    --muted:#777;
    --rule:#b9b9b9;
    --paper:#ffffff;
    --side:#6d6d6d;
  }
  *{margin:0;padding:0;box-sizing:border-box}
  html,body{width:863px;height:1200px;overflow:hidden;background:var(--paper)}
  body{font-family:"Open Sans",Arial,sans-serif;color:var(--text);position:relative}
  .page-title{position:absolute;left:36px;top:26px;font-family:"Oswald",Arial,sans-serif;font-weight:500;font-size:50px;line-height:1.3;color:var(--green);letter-spacing:.5px}
  .title-rule{position:absolute;left:36px;right:36px;height:2px;background:var(--green)}
  .title-rule.top{top:104px}
  .title-rule.bottom{top:110px;height:1px}
  .services{position:absolute;left:36px;right:36px;top:124px;display:grid;grid-template-columns:1fr 1fr 1fr;gap:22px}
  .service-heading{font-family:"Oswald",Arial,sans-serif;font-weight:500;font-size:26px;line-height:1.3;color:var(--green);text-align:center;padding-bottom:8px;border-bottom:2px solid var(--green);margin-bottom:6px;white-space:nowrap}
  .service-list{list-style:none}
  .service-list li{font-size:11.5px;line-height:1.3;padding:4px 0;border-bottom:1px dotted var(--rule)}
  .service-list li.accent{color:var(--orange);font-weight:600}
  .side-band{position:absolute;right:0;top:290px;width:18px;height:250px;background:var(--side)}
  .projects{position:absolute;left:36px;right:36px;top:462px;height:212px;display:grid;grid-template-columns:1fr 1fr 1fr;gap:12px}
  .project-photo{width:100%;height:100%}
  .photo-a{background:linear-gradient(180deg,#cfd6dc 0%,#a9a8a2 55%,#7f7a70 100%)}
  .photo-b{background:linear-gradient(180deg,#dfe4e6 0%,#b8b4aa 60%,#8b8779 100%)}
  .photo-c{background:linear-gradient(180deg,#9db7cf 0%,#a7a89a 45%,#7f8a6a 100%)}
  .section-title{position:absolute;left:36px;top:758px;font-family:"Oswald",Arial,sans-serif;font-weight:500;font-size:50px;line-height:1.3;color:var(--green)}
  .section-rule{position:absolute;left:36px;right:36px;top:836px;height:2px;background:var(--green)}
  .testimonial{position:absolute;left:36px;right:36px}
  .testimonial .mark{position:absolute;left:0;top:-16px;font-family:"Oswald",Arial,sans-serif;font-size:64px;color:var(--muted);line-height:1}
  .testimonial p{margin-left:44px;font-style:italic;font-size:12.5px;line-height:1.55}
  .testimonial .cite{margin-top:6px;text-align:right;font-size:12px;line-height:1.4}
  .t1{top:868px}
  .t2{top:1018px}
</style>
</head>
<body>
  <h1 class="page-title">Our Services</h1>
  <div class="title-rule top"></div>
  <div class="title-rule bottom"></div>

  <section class="services">
    <div class="service-column">
      <h2 class="service-heading">Architectural Services</h2>
      <ul class="service-list">
        <li>Building Planning &amp; Design</li>
        <li>Environmentally Conscious (LEED) Planning &amp; Design</li>
        <li class="accent">Budget Analysis and Cost Estimating</li>
        <li>Staff Input Collection &amp; Integration of Ideas</li>
        <li>Interior Design &amp; Color / Material Selection</li>
        <li>Value Engineering for Greatest Value to Taxpayers</li>
        <li>Historical Building Analysis and Planning</li>
      </ul>
    </div>
    <div class="service-column">
      <h2 class="service-heading">Engineering Services</h2>
      <ul class="service-list">
        <li>Mechanical Systems (HVAC &amp; Plumbing) Design</li>
        <li>Electrical Systems (Power &amp; Lighting) Design</li>
        <li>Technology Systems (Data Infrastructure &amp; Interface) Design</li>
        <li>Security Systems (Alarm, CCTV &amp; Door Access) Design</li>
        <li>Structural Systems Design &amp; Engineering</li>
        <li>Civil (Roadway, Drainage &amp; Utility) Design</li>
      </ul>
    </div>
    <div class="service-column">
      <h2 class="service-heading">Extended Services</h2>
      <ul class="service-list">
        <li>Capital Projects Fund Advising &amp; Planning</li>
        <li>Facility Maintenance Planning &amp; Scheduling</li>
        <li>Construction Observation &amp; Administration</li>
        <li>Energy Audits &amp; Energy Conservation Planning</li>
        <li>System Commissioning Services</li>
        <li>Post-Occupancy Evaluation</li>
      </ul>
    </div>
  </section>

  <div class="side-band"></div>

  <section class="projects">
    <div class="project-photo photo-a" role="img" aria-label="Photo of a school interior atrium with curved upper walkway"></div>
    <div class="project-photo photo-b" role="img" aria-label="Photo of a bright school commons area with large windows"></div>
    <div class="project-photo photo-c" role="img" aria-label="Aerial photo of a completed school campus"></div>
  </section>

  <h2 class="section-title">Testimonials</h2>
  <div class="section-rule"></div>

  <blockquote class="testimonial t1">
    <span class="mark">&ldquo;</span>
    <p>As the district's contact person for the project, I worked closely with Halvernquist-Odell through the development, construction, and as-built phases. I found them to be highly knowledgeable of educational needs, extremely competent, very responsive, incredibly organized, patient and enjoyable to work with. Above all, I was impressed with how well they listened.</p>
    <div class="cite">Dr. Marcus T. Wendell – Superintendent<br>Northfield Ridge Community Schools</div>
  </blockquote>

  <blockquote class="testimonial t2">
    <span class="mark">&ldquo;</span>
    <p>They have provided the necessary assistance in every phase of each project to ensure that the district's expectations are met. They are excellent problem solvers, while at the same time, minimizing the need for change orders. Halvernquist-Odell is committed to making sure that the customer is completely satisfied and comfortable with the construction and performance of the new facility/project.</p>
    <div class="cite">Daniel R. Prescott – Assistant Superintendent<br>Northfield Ridge Community Schools</div>
  </blockquote>
</body>
</html>
```